NEW Gummy line needs fabulous, eye catching, juicy packaging!

***PLEASE NOTE: this is ONE bag, with THREE FLAVORS in the one bag. We are looking for a design that visually represents the three flavors in the bag*****

We are a well established cannabis company in Washington State, looking to launch a new line of gummies that are more affordable for the marketplace as people struggle with rising prices. The new brand name is "Tinsel & Company" and the product will be called "Lantern Meadow" - every bag is a MULTI-FLAVOR pack of 3 flavors (Washington State Cherry, Blue Elderberry, Royal Purple Raspberry) and an example of the gummy berry shape has been uploaded. We are looking for the packaging to reflect the three fruit flavors inside the bag - and can also have images of the shape of the gummies inside - I will upload an example of the gummy shape for reference also.

There are a number of "required elements" for state compliance in our state, so I will upload an example of our current 'VOLTA' brand APPLE flavor packaging so you can see how those "required elements" appear (Not for Kids icon, 21+ icon, the weight, the serving size information, 100mg THC/bag, and all the warning language is the same for this product as the APPLE example bag I have uploaded). Please reference the APPLE packaging for the icons and copy ONLY - this contest is for Tinsel & Company which is a new brand and we would like to see completely new concepts as both brands will be sold in the same stores.

We are most concerned with the visual concept - so no need to get all the placements, or all of the required elements for this initial contest, we can work together to perfect it once chosen. But in past competitions, designers have found it helpful to know for placement.

***NO CANNABIS IMAGERY PLEASE***

The products are sold in specialty dispensaries so customers are aware the products contain THC. We are more so looking for retail packaging that is trendy, modern, eye catching and enticing for a gummy food product.

**I have also uploaded a "PIPWICKS" package and a "ZUNK" - they are competitors - so we don't want to look like them, but providing it for inspiration where they mix the candy and the fruit, which can also be an idea for us.

PLEASE NOTE: This is a one bag design - each bag contains three flavors. So the design should reflect an mix of the 3 berry flavors

I am extending the deadline as we were able to push our print deadline back and I would like to give designers the weekend for their submissions. I also clarified the brief - ONE BAG, 3 FLAVORS inside - and hoping this is helpful for the designers also.

Target Market(s)

21+ THC Gummy lovers in Washington state

Industry/Entity Type

Cannabis Edibles

Requirements
Must have
• BOLD, eye catching, delicious design that is appealing for a gummy product (berries and product image a PLUS)
Nice to have
• incorporate the berries as visual, orchard visuals, organic but vibrant and juicy and fun
Should not have
• NO CANNABIS IMAGERY PLS

```html
<!DOCTYPE html>
<html lang="en">
<head>
<meta charset="utf-8">
<title>Tinsel &amp; Company — Lantern Meadow Gummies</title>
<link href="https://fonts.googleapis.com/css2?family=Barlow+Condensed:wght@500;600;700&family=Barlow:wght@600;700&family=Bitter:wght@700;800&display=swap" rel="stylesheet">
<style>
  :root {
    --page: #ffffff;
    --bag-top: #8e96c6;
    --bag-bottom: #3d416f;
    --panel: rgba(176, 181, 214, 0.55);
    --ink: #141414;
    --berry: #a52a6c;
    --white: #ffffff;
    --alert: #d81f2a;
    --badge-yellow: #f3e61d;
  }
  * { margin: 0; padding: 0; box-sizing: border-box; }
  html, body { width: 1200px; height: 1200px; overflow: hidden; background: var(--page); }
  .canvas { position: relative; width: 1200px; height: 1200px; }
  .bag {
    position: absolute; left: 206px; top: 47px; width: 797px; height: 1128px;
    background: linear-gradient(180deg, var(--bag-top) 0%, #7880b3 40%, var(--bag-bottom) 100%);
    overflow: hidden;
  }
  .label-panel {
    position: absolute; left: 155px; top: 390px; width: 490px; height: 620px;
    background: var(--panel);
  }
  .fruit-art { position: absolute; inset: 0; width: 100%; height: 100%; }
  .compliance { position: absolute; left: 192px; top: 42px; display: flex; align-items: flex-start; gap: 16px; }
  .age-badge { width: 94px; height: 94px; }
  .kids-block { display: flex; flex-direction: column; align-items: flex-start; gap: 8px; }
  .kids-badge { width: 72px; height: 52px; }
  .emergency {
    font-family: "Barlow", sans-serif; font-weight: 700; font-size: 10px;
    color: var(--alert); line-height: 1.3; letter-spacing: 0.04em;
  }
  .brand-name {
    position: absolute; left: 0; right: 0; top: 200px; text-align: center;
    font-family: "Barlow Condensed", sans-serif; font-weight: 700; color: var(--ink);
    font-size: 108px; line-height: 0.97; letter-spacing: 0.01em; text-transform: uppercase;
  }
  .product-name {
    position: absolute; left: 155px; width: 490px; top: 528px; text-align: center;
    font-family: "Barlow Condensed", sans-serif; font-weight: 600; color: var(--berry);
    font-size: 116px; line-height: 0.88; text-transform: uppercase;
  }
  .product-type {
    position: absolute; left: 155px; width: 490px; top: 752px; text-align: center;
    font-family: "Barlow", sans-serif; font-weight: 700; color: var(--white);
  }
  .product-type .line-1 { font-size: 22px; letter-spacing: 0.05em; display: block; }
  .product-type .line-2 { font-size: 30px; letter-spacing: 0.14em; display: block; margin-top: 4px; }
  .dose { position: absolute; left: 190px; top: 850px; font-family: "Bitter", serif; color: #1c1c22; }
  .dose .thc { font-size: 19px; font-weight: 800; }
  .dose .count { display: flex; align-items: center; gap: 12px; margin-top: 22px; }
  .dose .count-num { font-size: 40px; font-weight: 800; line-height: 1; }
  .dose .count-label { font-size: 14px; font-weight: 700; line-height: 1.25; }
  .dose .strain { font-size: 18px; font-weight: 800; margin-top: 26px; margin-left: 22px; }
  .gummy-art { position: absolute; left: 353px; top: 830px; width: 235px; height: 175px; }
  .net-wt {
    position: absolute; right: 66px; bottom: 26px;
    font-family: "Barlow Condensed", sans-serif; font-weight: 700; font-size: 24px; color: var(--white);
  }
</style>
</head>
<body>
<main class="canvas">
  <section class="bag">
    <div class="label-panel"></div>

    <svg class="fruit-art" viewBox="0 0 797 1128" role="img" aria-label="Glossy photographed cherries, blackberries, elderberries and green leaves framing the bag edges">
      <defs>
        <radialGradient id="cherry" cx="34%" cy="30%" r="72%">
          <stop offset="0%" stop-color="#ffd0d0"/><stop offset="12%" stop-color="#f0484f"/><stop offset="55%" stop-color="#c41a28"/><stop offset="100%" stop-color="#6e0a16"/>
        </radialGradient>
        <radialGradient id="blackberry" cx="36%" cy="30%" r="72%">
          <stop offset="0%" stop-color="#c2a6e0"/><stop offset="15%" stop-color="#8a68b4"/><stop offset="60%" stop-color="#5a4088"/><stop offset="100%" stop-color="#2f1f4e"/>
        </radialGradient>
        <radialGradient id="elder" cx="36%" cy="30%" r="72%">
          <stop offset="0%" stop-color="#8a88b8"/><stop offset="15%" stop-color="#44426c"/><stop offset="60%" stop-color="#22213e"/><stop offset="100%" stop-color="#0e0d1c"/>
        </radialGradient>
        <linearGradient id="leaf" x1="0" y1="0" x2="1" y2="1">
          <stop offset="0%" stop-color="#7aa874"/><stop offset="100%" stop-color="#2c5030"/>
        </linearGradient>
      </defs>
      <circle cx="62" cy="68" r="44" fill="url(#cherry)"/>
      <ellipse cx="770" cy="82" rx="50" ry="22" fill="url(#leaf)"/>
      <circle cx="775" cy="130" r="38" fill="url(#elder)"/>
      <ellipse cx="78" cy="295" rx="34" ry="44" fill="url(#blackberry)"/>
      <ellipse cx="28" cy="470" rx="66" ry="108" fill="url(#cherry)"/>
      <ellipse cx="116" cy="590" rx="36" ry="40" fill="url(#blackberry)"/>
      <ellipse cx="780" cy="280" rx="36" ry="105" fill="url(#leaf)"/>
      <ellipse cx="720" cy="460" rx="82" ry="140" fill="url(#blackberry)"/>
      <ellipse cx="110" cy="790" rx="110" ry="56" fill="url(#leaf)" transform="rotate(-45 110 790)"/>
      <ellipse cx="38" cy="960" rx="78" ry="125" fill="url(#elder)"/>
      <circle cx="703" cy="683" r="24" fill="url(#elder)"/>
      <circle cx="724" cy="846" r="35" fill="url(#cherry)"/>
      <ellipse cx="795" cy="1075" rx="55" ry="92" fill="url(#cherry)"/>
      <ellipse cx="232" cy="1095" rx="52" ry="36" fill="url(#blackberry)"/>
      <ellipse cx="418" cy="1050" rx="78" ry="38" fill="url(#leaf)"/>
      <circle cx="412" cy="1110" r="40" fill="url(#elder)"/>
    </svg>

    <div class="compliance">
      <svg class="age-badge" viewBox="0 0 96 96" role="img" aria-label="Age compliance badge">
        <polygon points="48,2 94,48 48,94 2,48" fill="var(--white)" stroke="var(--ink)" stroke-width="4"/>
        <polygon points="48,10 86,48 48,86 10,48" fill="var(--badge-yellow)"/>
      </svg>
      <div class="kids-block">
        <svg class="kids-badge" viewBox="0 0 72 52" role="img" aria-label="Child safety badge">
          <rect x="0" y="0" width="72" height="52" rx="6" fill="var(--alert)"/>
        </svg>
        <p class="emergency">EMERGENCY<br>(800) 555 0199</p>
      </div>
    </div>

    <h1 class="brand-name">Tinsel<br>&amp; Company</h1>

    <h2 class="product-name">Lantern<br>Meadow</h2>

    <p class="product-type">
      <span class="line-1">CANNABIS INFUSED</span>
      <span class="line-2">GUMMIES</span>
    </p>

    <div class="dose">
      <p class="thc">100MG THC</p>
      <div class="count">
        <span class="count-num">10</span>
        <span class="count-label">PIECES<br>PER BAG</span>
      </div>
      <p class="strain">INDICA</p>
    </div>

    <svg class="gummy-art" viewBox="0 0 235 175" role="img" aria-label="Pile of glossy raspberry-shaped gummies in purple, magenta, red, orange and blue">
      <defs>
        <radialGradient id="gPurple" cx="38%" cy="30%" r="72%"><stop offset="0%" stop-color="#e0b0e6"/><stop offset="15%" stop-color="#a35aa8"/><stop offset="100%" stop-color="#4e1c56"/></radialGradient>
        <radialGradient id="gMagenta" cx="38%" cy="30%" r="72%"><stop offset="0%" stop-color="#ffb0cc"/><stop offset="15%" stop-color="#e04a7e"/><stop offset="100%" stop-color="#7c173c"/></radialGradient>
        <radialGradient id="gRed" cx="38%" cy="30%" r="72%"><stop offset="0%" stop-color="#ffc0c0"/><stop offset="15%" stop-color="#ff4a4a"/><stop offset="100%" stop-color="#b00c18"/></radialGradient>
        <radialGradient id="gOrange" cx="38%" cy="30%" r="72%"><stop offset="0%" stop-color="#ffd0b8"/><stop offset="15%" stop-color="#ff7a5a"/><stop offset="100%" stop-color="#d0261e"/></radialGradient>
        <radialGradient id="gBlue" cx="38%" cy="30%" r="72%"><stop offset="0%" stop-color="#e0f6ff"/><stop offset="15%" stop-color="#7fd6f5"/><stop offset="100%" stop-color="#2490c4"/></radialGradient>
      </defs>
      <ellipse cx="62" cy="72" rx="42" ry="38" fill="url(#gMagenta)"/>
      <ellipse cx="146" cy="44" rx="44" ry="42" fill="url(#gRed)"/>
      <ellipse cx="196" cy="130" rx="40" ry="30" fill="url(#gBlue)"/>
      <ellipse cx="132" cy="116" rx="44" ry="42" fill="url(#gOrange)"/>
      <ellipse cx="52" cy="140" rx="48" ry="32" fill="url(#gPurple)"/>
    </svg>

    <p class="net-wt">NET WT 2.2 OZ (62G)</p>
  </section>
</main>
</body>
</html>
```